Wellness, Purpose, and the Quiet Path Research Program Website

Overview: This website will serve a new research program (Wellness, Purpose, and the Quiet Path) at the Thornbury University School of Medicine. I want a clean, intuitive design that has a navigation bar, but uses icons/graphic buttons to link to the main pages. In an attached Word document, I have provided a basic information architecture for the site, understanding that this project would just generate graphics and code for the 3 pages. I highlighted the 3 pages I'd like designed.
Target market: People who want to participate in our research, or contribute grant funding to specific projects.
Number of page: The design project focuses on 3 pages, but the site must accommodate 6 pages with top-level links. See attached Word doc.
Logo and website header: Please integrate our logo in the header. I've uploaded it as a png file--both with the name of the website and with just the logo image. I imaging the logo would look great in a banner set against an image of a mountain. The two main design themes I want to see included are nature and healthcare.
Text content: I have not yet provided text. Use some dummy text.
Technical Specifications:
- Build using WordPress. We will host this site ourselves on HostBarrow using WordPress.
- The design package must be coded.
- The template must be responsive to different platforms (e.g., computer, mobile phone, Zelvo).
Thank you! I look forward to seeing your designs.
- Ned

```html
<!DOCTYPE html>
<html lang="en">
<head>
<meta charset="utf-8">
<title>Wellness, Purpose, and the Quiet Path Research Program</title>
<link href="https://fonts.googleapis.com/css2?family=Poppins:wght@400;600;700&family=Lato:wght@400;700;900&display=swap" rel="stylesheet">
<style>
:root{
  --page:#e9e6e1;
  --white:#ffffff;
  --blue:#1b5c99;
  --blue-dark:#17456f;
  --green:#78ae33;
  --green-dark:#5f922a;
  --teal:#2f8a78;
  --text:#555a60;
  --ink:#111111;
}
*{margin:0;padding:0;box-sizing:border-box}
html,body{width:1200px;height:5189px;overflow:hidden;background:var(--page)}
body{font-family:"Lato",sans-serif;position:relative}
.site{position:absolute;left:300px;top:178px;width:600px;height:4832px;background:var(--white);overflow:hidden}

.site-header{height:152px;display:flex;align-items:center;justify-content:space-between;padding:0 26px 0 24px;background:var(--white)}
.brand{display:flex;align-items:center;gap:14px}
.brand-dot{width:62px;height:62px;border-radius:50%;background:var(--blue)}
.brand-name{font-family:"Poppins",sans-serif;font-weight:600;font-size:17px;line-height:1.25;color:var(--blue);max-width:340px}
.menu-toggle{width:60px;height:60px;border:3px solid var(--green);border-radius:50%;display:flex;flex-direction:column;align-items:center;justify-content:center;gap:6px}
.menu-toggle span{width:26px;height:3px;background:var(--green);border-radius:2px}

.hero{position:relative;height:639px}
.hero-photo{position:absolute;inset:0;background:linear-gradient(180deg,#c9d5de 0%,#8fa6b4 22%,#4e7a5c 40%,#2fb3b4 55%,#3c7d3c 70%,#6fae3a 100%)}
.hero-brand{position:absolute;left:28px;top:250px;display:flex;align-items:center;gap:16px}
.hero-brand .brand-dot{width:100px;height:100px;background:transparent;border:3px solid var(--white)}
.hero-brand .brand-name{color:var(--white);font-size:19px;max-width:400px}
.hero-wave{position:absolute;left:0;bottom:0;width:600px;height:70px}

.vision{height:1263px;padding-top:60px;text-align:center}
.section-title{font-family:"Poppins",sans-serif;font-size:38px;font-weight:400;color:var(--blue)}
.section-title strong{font-weight:700}
.venn{display:block;margin:18px auto 0;width:600px;height:520px}
.venn-label{font-family:"Lato",sans-serif;font-weight:700;font-size:20px;fill:var(--white)}
.vision-text{margin:30px 24px 0;font-size:19.5px;line-height:40px;color:var(--text);text-align:justify}
.btn{display:inline-block;margin-top:36px;width:232px;height:61px;line-height:61px;border-radius:31px;background:var(--green);color:var(--white);font-size:20px;font-weight:700;letter-spacing:.5px}

.explore{height:1870px;background:var(--green);padding-top:76px;text-align:center}
.explore .section-title{color:var(--white);font-size:38px}
.cards{margin-top:36px;padding:0 22px;display:flex;flex-direction:column;gap:38px}
.card{background:var(--white);border-radius:4px;overflow:hidden;height:513px}
.card-photo{height:416px}
.photo-people{background:linear-gradient(180deg,#2e62b8 0%,#79a7d9 40%,#9cc53c 70%,#4c8c1f 100%)}
.photo-research{background:linear-gradient(120deg,#a88c6a 0%,#8a7a68 30%,#3f7fd1 55%,#b7cdea 100%)}
.photo-faq{background:linear-gradient(180deg,#d98b45 0%,#f2c07a 35%,#6b5a45 60%,#3d3a36 100%)}
.card-title{height:97px;line-height:97px;font-size:30px;font-weight:700;color:var(--ink)}

.site-footer{position:absolute;left:0;top:3900px;width:600px;height:932px;background:linear-gradient(180deg,#2d6aa6 0%,#27629a 45%,#1f4f7e 80%,#1b4468 100%);color:var(--white);padding:198px 26px 0}
.footer-wave{position:absolute;left:0;top:-2px;width:600px;height:90px}
.footer-brand{display:flex;align-items:center;gap:16px}
.footer-brand .brand-dot{width:88px;height:88px;background:transparent;border:3px solid var(--white)}
.footer-brand .brand-name{color:var(--white);font-size:17px}
.footer-title{margin-top:78px;font-size:30px;font-weight:700}
.contact{list-style:none;margin-top:30px}
.contact li{display:flex;gap:18px;font-size:19px;line-height:26px;margin-bottom:46px}
.contact svg{flex:none;width:20px;height:22px;margin-top:3px}
.contact li:nth-child(2){margin-bottom:40px}
.footer-rule{border:0;border-top:1px solid rgba(255,255,255,.35);margin-top:72px}
.copyright{text-align:center;font-size:19px;line-height:32px;margin-top:42px}
</style>
</head>
<body>
<div class="site">
  <header class="site-header">
    <div class="brand">
      <span class="brand-dot"></span>
      <span class="brand-name">Wellness, Purpose, and the Quiet Path Research Program</span>
    </div>
    <div class="menu-toggle"><span></span><span></span><span></span></div>
  </header>

  <section class="hero">
    <div class="hero-photo" role="img" aria-label="Mountain valley with a turquoise lake and pine forest"></div>
    <div class="hero-brand">
      <span class="brand-dot"></span>
      <span class="brand-name">Wellness, Purpose, and the Quiet Path Research Program</span>
    </div>
    <svg class="hero-wave" viewBox="0 0 600 70" preserveAspectRatio="none">
      <path d="M0 30 C150 -10 330 90 600 10 L600 70 L0 70Z" fill="#ffffff"/>
      <path d="M0 30 C150 -10 330 90 600 10" fill="none" stroke="#1b5c99" stroke-width="6"/>
      <path d="M0 42 C160 5 340 95 600 22" fill="none" stroke="#78ae33" stroke-width="6"/>
    </svg>
  </section>

  <section class="vision">
    <h2 class="section-title"><strong>Vision</strong> Statement</h2>
    <svg class="venn" viewBox="0 0 600 520">
      <circle cx="290" cy="152" r="152" fill="#2f8a78" opacity=".95"/>
      <circle cx="411" cy="338" r="152" fill="#1b5c99" opacity=".9"/>
      <circle cx="182" cy="338" r="152" fill="#78ae33" opacity=".88"/>
      <g fill="none" stroke="#ffffff" stroke-width="2" stroke-dasharray="2 5" opacity=".8">
        <circle cx="290" cy="152" r="138"/><circle cx="411" cy="338" r="138"/><circle cx="182" cy="338" r="138"/>
      </g>
      <g fill="none" stroke="#ffffff" stroke-width="3">
        <path d="M290 105 c-6-12-26-10-26 5 c0 12 26 26 26 26 s26-14 26-26 c0-15-20-17-26-5z"/>
        <circle cx="182" cy="300" r="20"/><circle cx="182" cy="300" r="8"/>
        <path d="M400 300 a20 20 0 1 1 22 0 v12 h-22z"/>
      </g>
      <text class="venn-label" x="290" y="180" text-anchor="middle">Healthcare</text>
      <text class="venn-label" x="182" y="374" text-anchor="middle">Spiritual Life</text>
      <text class="venn-label" x="411" y="378" text-anchor="middle">Values</text>
    </svg>
    <p class="vision-text">Lorem ipsum dolor sit amet, consectetur adipiscing elit, sed do eiusmod tempor incididunt ut labore et dolore magna aliqua. Ut enim ad minim veniam, quis nostrud exercitation ullamco laboris nisi ut aliquip ex ea commodo consequat. Duis aute irure dolor in reprehenderit in voluptate velit esse cillum dolore eu fugiat nulla pariatur. Sed ut perspiciatis unde omnis iste natus error sit voluptatem accusantium doloremque laudantium, totam rem aperiam, eaque ipsa quae ab illo inventore veritatis</p>
    <a class="btn">READ MORE</a>
  </section>

  <section class="explore">
    <h2 class="section-title"><strong>Explore our</strong> Program</h2>
    <div class="cards">
      <article class="card"><div class="card-photo photo-people" role="img" aria-label="Wind turbines above a green meadow with trees"></div><h3 class="card-title">People</h3></article>
      <article class="card"><div class="card-photo photo-research" role="img" aria-label="Climber on a rock overhang against a blue sky"></div><h3 class="card-title">Research Projects</h3></article>
      <article class="card"><div class="card-photo photo-faq" role="img" aria-label="Runner on a tree-lined road at sunset"></div><h3 class="card-title">FAQs</h3></article>
    </div>
  </section>

  <footer class="site-footer" role="img" aria-label="Blue-tinted mountain and lake landscape">
    <svg class="footer-wave" viewBox="0 0 600 90" preserveAspectRatio="none">
      <path d="M0 0 H600 V20 C420 70 240 10 0 60Z" fill="#78ae33"/>
      <path d="M0 60 C240 10 420 70 600 20" fill="none" stroke="#1b8ad6" stroke-width="8"/>
    </svg>
    <div class="footer-brand">
      <span class="brand-dot"></span>
      <span class="brand-name">Wellness, Purpose, and the Quiet Path Research Program</span>
    </div>
    <h3 class="footer-title">Contact Us</h3>
    <ul class="contact">
      <li><svg viewBox="0 0 20 22"><path d="M10 0a8 8 0 0 0-8 8c0 6 8 14 8 14s8-8 8-14a8 8 0 0 0-8-8zm0 11a3 3 0 1 1 0-6 3 3 0 0 1 0 6z" fill="#fff"/></svg><span>Address:<br>Lorem ipsum dolor sit amet, consectetur adipiscing elit, sed</span></li>
      <li><svg viewBox="0 0 20 22"><path d="M4 2l4 0 2 5-3 2c1 3 3 5 6 6l2-3 5 2v4c0 1-1 2-2 2C9 20 2 13 2 4c0-1 1-2 2-2z" fill="#fff"/></svg><span>Phone :<br>555 - 014 - 2290</span></li>
      <li><svg viewBox="0 0 20 22"><path d="M1 5h18v13H1z" fill="#fff"/><path d="M1 5l9 7 9-7" fill="none" stroke="#27629a" stroke-width="2"/></svg><span>Email :<br>info@quietpathresearch.org</span></li>
    </ul>
    <hr class="footer-rule">
    <p class="copyright">© Copyright 2021 Company Name .<br>All Rights Reserved</p>
  </footer>
</div>
</body>
</html>
```